依頼詳細
病院にて使用する封筒デザインの募集です
記載項目
医療法人 栄樹会 ベルミナ中央病院 BELMINA CENTRAL HOSPITAL
【英語表記は小さめで】

診療科目 内科、呼吸器内科、消化器内科、循環器内科、放射線科、リハビリテーション科、精神科、心療内科

希望イメージ
シンプル 複雑
単色 カラフル
暗い 明るい
日常 高級
遊び心 厳粛
未来的 伝統的
女性的 男性的
希望する色
自由な発想でご提案ください
納品ファイル
• 高解像度JPG (.jpg)
• イラストレーター形式 (.ai)
• フォトショップ形式 (.psd)
補足説明
A4が入る大封筒と
通常サイズの小封筒の2種類をご提案下さい

看板のデザインも募集しておりますので
合わせてご応募頂けると助かります
住所電話番号を追記します

住所 鹿児島県鹿児島市緑葉台2丁目37番8号
TEL 099-555-0142
FAX 099-555-0143
角2(240×332mm)と長3(120×235mm)
でお願い致します

aiファイルも追加致します
吹き抜け壁面と受付カウンター裏の写真を追加します
全体の色使いに関してはロゴの色にこだわらずご提案下さい
建物の色や、吹き抜け壁面の色や形をモチーフにしたものでも構いません
よろしくお願い致します
ご提案ありがとうございます
ロゴカラーに沿ったもの、
吹き抜けカラーに沿ったものをご提案頂いておりますが

合わせて病院の外壁色(赤茶と白)
を基調としたものも募集しております
よろしくお願い致します
■ 選んだ理由

病院のイメージにあっていたので選ばせて頂きました

■ 提案者全員のお礼・コメント

たくさんのご提案を頂きありがとうございました
また利用させて頂きます

```html
<!DOCTYPE html>
<html lang="ja">
<head>
<meta charset="utf-8">
<title>ベルミナ中央病院 長3封筒</title>
<link rel="stylesheet" href="https://fonts.googleapis.com/css2?family=Noto+Sans+JP:wght@400;500;700&family=Noto+Serif+JP:wght@500&display=swap">
<style>
  :root {
    --paper: #ffffff;
    --envelope: #f7ebbd;
    --envelope-edge: #d9c98f;
    --brand-green: #3fa64a;
    --text-green: #2f8f3c;
    --ink: #4a5a44;
  }
  * { margin: 0; padding: 0; box-sizing: border-box; }
  html, body { width: 849px; height: 1200px; overflow: hidden; background: var(--paper); }
  .canvas { position: relative; width: 849px; height: 1200px; font-family: "Noto Sans JP", sans-serif; }
  .envelope-shape { position: absolute; inset: 0; }
  .flap-text {
    position: absolute; left: 212px; width: 476px; text-align: center; white-space: nowrap;
    transform: rotate(180deg); color: var(--text-green);
  }
  .flap-name { top: 122px; font-family: "Noto Serif JP", serif; font-weight: 500; font-size: 18px; letter-spacing: 0.1em; }
  .flap-english { top: 30px; font-size: 8px; letter-spacing: 0.12em; }
  .brand-lockup {
    position: absolute; left: 222px; top: 930px; width: 190px; text-align: center; color: var(--brand-green);
    white-space: nowrap;
  }
  .brand-dot { display: block; width: 42px; height: 42px; margin: 0 auto 10px; border-radius: 50%; background: var(--brand-green); }
  .brand-english { font-size: 8px; letter-spacing: 0.06em; font-weight: 500; }
  .brand-name { font-size: 19px; font-weight: 500; letter-spacing: 0.02em; margin-top: 2px; line-height: 1.3; }
  .brand-corp { font-size: 8px; font-weight: 500; margin-top: 2px; }
  .contact-block {
    position: absolute; left: 458px; top: 960px; width: 222px; color: var(--text-green);
    font-size: 9px; line-height: 1.6; white-space: nowrap;
  }
  .departments-title { font-weight: 700; }
  .departments-list { margin-bottom: 12px; }
  .address, .phone { color: var(--ink); }
</style>
</head>
<body>
<div class="canvas">
  <svg class="envelope-shape" width="849" height="1200" viewBox="0 0 849 1200" aria-hidden="true">
    <polygon points="212,44 232,14 668,14 688,44 688,184 212,184" fill="var(--envelope)" stroke="var(--envelope-edge)" stroke-width="1"/>
    <rect x="212" y="184" width="476" height="942" fill="var(--envelope)" stroke="var(--envelope-edge)" stroke-width="1"/>
  </svg>

  <div class="flap-text flap-english">BELMINA CENTRAL HOSPITAL</div>
  <div class="flap-text flap-name">医療法人 栄樹会　ベルミナ中央病院</div>

  <div class="brand-lockup">
    <span class="brand-dot"></span>
    <div class="brand-english">BELMINA CENTRAL HOSPITAL</div>
    <div class="brand-name">ベルミナ中央病院</div>
    <div class="brand-corp">医療法人 栄樹会</div>
  </div>

  <div class="contact-block">
    <div class="departments-title">診療科目</div>
    <div class="departments-list">内科、呼吸器内科、消化器内科、循環器内科、<br>放射線科、リハビリテーション科、精神科、心療内科</div>
    <div class="address">鹿児島県鹿児島市緑葉台2丁目37番8号</div>
    <div class="phone">TEL 099-555-0142　FAX 099-555-0143</div>
  </div>
</div>
</body>
</html>
```